Photographer Card

I'm currently doing freelance photography and i need a creative design name card especially when i attend events.
I require a design that makes a STATEMENT.
Simple, elegant and nothing like the usual name cards ive seen around (Example: with a camera/tripod etc in the design).

Photographer: Dorian VP
Mobile: +65 84126957
E-mail: Dorian.VP.Photography@mailvista.net
Facebook: www.friendlane.net/dorian.vp.photography

Thanks for your time and hope it will turn out well! :)
Updates

Thanks for all your inputs!

Im liking the cursive feel.

Id prefer not to include the title "freelance"  :)

Also, im looking for a logo to establish myself

http://www.artmosaic.net/art/Cotton-Business-Card-583021746

Hi all! Thanks for the designs

"Capturing magical moments"
"Capturing magical moments that are gone forever"

Back design can be in big font "look HERE"

Maybe with focusing box 

Names can be played with horizontal and vertical.

Industry/Entity Type

Camera

Font styles to use
Script

```html
<!DOCTYPE html>
<html lang="en">
<head>
<meta charset="utf-8">
<title>Dorian VP — Photographer Card</title>
<link rel="stylesheet" href="https://fonts.googleapis.com/css2?family=Great+Vibes&family=Raleway:wght@200;300&display=swap">
<style>
  :root {
    --card-bg: #070b0c;
    --ink: #f4f4f2;
    --ink-soft: #e2e2df;
    --glow: rgba(255, 255, 255, 0.35);
  }
  * { margin: 0; padding: 0; box-sizing: border-box; }
  html, body {
    width: 1200px;
    height: 704px;
    overflow: hidden;
    background: var(--card-bg);
  }
  .card {
    position: relative;
    width: 1200px;
    height: 704px;
    background: var(--card-bg);
    color: var(--ink);
    font-family: "Raleway", sans-serif;
    font-weight: 200;
  }
  .script-name {
    position: absolute;
    left: 130px;
    top: 572px;
    transform-origin: 0 0;
    transform: rotate(-90deg);
    font-family: "Great Vibes", cursive;
    font-weight: 400;
    font-size: 170px;
    line-height: 1;
    white-space: nowrap;
    color: var(--ink);
    text-shadow: 0 0 6px var(--glow), 0 0 18px rgba(255, 255, 255, 0.12);
  }
  .initials {
    position: absolute;
    left: 342px;
    top: 432px;
    font-size: 108px;
    line-height: 1;
    letter-spacing: 2px;
  }
  .title {
    position: absolute;
    left: 233px;
    top: 510px;
    font-size: 79px;
    line-height: 1;
    letter-spacing: 1px;
  }
  .mobile {
    position: absolute;
    left: 714px;
    top: 514px;
    transform-origin: 0 0;
    transform: rotate(-90deg);
    font-size: 40px;
    line-height: 1;
    letter-spacing: 3px;
    white-space: nowrap;
  }
  .brand {
    position: absolute;
    left: 760px;
    top: 71px;
    width: 438px;
    height: 443px;
    background: var(--ink);
    display: flex;
    align-items: center;
    justify-content: center;
  }
  .brand-name {
    color: var(--card-bg);
    font-size: 58px;
    font-weight: 200;
    line-height: 1;
    letter-spacing: 3px;
    white-space: nowrap;
  }
  .contact {
    position: absolute;
    top: 628px;
    font-size: 29px;
    line-height: 1;
    color: var(--ink-soft);
    white-space: nowrap;
  }
  .contact-email { left: 28px; letter-spacing: 1px; }
  .contact-social { right: 34px; letter-spacing: 1.5px; }
</style>
</head>
<body>
  <main class="card">
    <div class="script-name">Dorian</div>
    <div class="initials">VP</div>
    <div class="title">photographer</div>
    <div class="mobile">Mobile: +65 84126957</div>

    <div class="brand">
      <span class="brand-name">Dorian VP</span>
    </div>

    <div class="contact contact-email">Dorian.VP.Photography@mailvista.net</div>
    <div class="contact contact-social">friendlane.net/dorian.vp.photography</div>
  </main>
</body>
</html>
```